Custom Business Card Design

We are looking for a raised spot logo design to use with Tavu.com. We will provide the logo files. Should be a front and back design. We want to implement the house into the back design using the same colors as the logo through out. Something VERY cool!

```html
<!DOCTYPE html>
<html lang="en">
<head>
<meta charset="utf-8">
<title>Tavu.com Business Card</title>
<link href="https://fonts.googleapis.com/css2?family=Open+Sans:wght@400;600;700&display=swap" rel="stylesheet">
<style>
  :root {
    --backdrop: #2c2d30;
    --red-light: #f57c84;
    --red: #ee4c55;
    --blue: #2f7cc4;
    --blue-dark: #1f5fa6;
    --white: #ffffff;
    --text: #4a4a4a;
    --divider: #d9d9d9;
  }
  * { box-sizing: border-box; margin: 0; padding: 0; }
  html, body { width: 1200px; height: 840px; overflow: hidden; }
  body {
    background: var(--backdrop);
    font-family: "Open Sans", Arial, sans-serif;
  }
  .canvas {
    position: relative;
    width: 1200px;
    height: 840px;
  }
  .card {
    position: absolute;
    left: 320px;
    width: 560px;
    height: 320px;
    overflow: hidden;
    box-shadow: 0 10px 30px rgba(0,0,0,.45);
  }
  .card-front {
    top: 80px;
    background: linear-gradient(110deg, var(--red-light) 0%, var(--red) 55%, var(--red) 100%);
    display: flex;
    align-items: center;
    justify-content: center;
  }
  .card-back {
    top: 440px;
    background: var(--white);
  }
  .brand {
    display: flex;
    align-items: center;
    gap: 12px;
    font-weight: 700;
    line-height: 1;
  }
  .brand-mark {
    width: 0.55em;
    height: 0.55em;
    background: currentColor;
  }
  .card-front .brand { color: var(--white); font-size: 64px; }
  .card-back .brand {
    position: absolute;
    left: 52px;
    top: 132px;
    color: var(--blue);
    font-size: 44px;
  }
  .top-band {
    position: absolute;
    left: 0; top: 0;
    width: 100%; height: 8px;
    background: var(--blue);
  }
  .bottom-band {
    position: absolute;
    left: 0; bottom: 0;
    width: 100%; height: 26px;
    background: linear-gradient(90deg, var(--blue-dark), var(--blue));
  }
  .divider {
    position: absolute;
    left: 306px; top: 40px;
    width: 1px; height: 220px;
    background: var(--divider);
  }
  .contact {
    position: absolute;
    left: 330px;
    top: 52px;
    color: var(--text);
    font-size: 14px;
    line-height: 19px;
  }
  .contact-name { color: var(--blue); font-weight: 700; font-size: 15px; }
  .contact-role { color: var(--red); font-weight: 600; font-size: 15px; margin-bottom: 4px; }
  .contact-address { margin-bottom: 8px; }
  .contact-list { list-style: none; }
  .contact-list li { display: flex; align-items: center; gap: 8px; }
  .contact-list svg { width: 12px; height: 12px; fill: var(--blue-dark); flex: none; }
</style>
</head>
<body>
<div class="canvas">
  <section class="card card-front">
    <div class="brand"><span class="brand-mark"></span>Tavu.com</div>
  </section>

  <section class="card card-back">
    <div class="top-band"></div>
    <div class="brand"><span class="brand-mark"></span>Tavu.com</div>
    <div class="divider"></div>
    <div class="contact">
      <div class="contact-name">ALEX RIVERS</div>
      <div class="contact-role">CEO/FOUNDER</div>
      <div class="contact-address">42 Maple Row<br>Juneau, Alaska 34570</div>
      <ul class="contact-list">
        <li><svg viewBox="0 0 12 12"><path d="M2 1h2l1 3-1.5 1a6 6 0 0 0 3.5 3.5L8 7l3 1v2a1 1 0 0 1-1 1A9 9 0 0 1 1 2a1 1 0 0 1 1-1z"/></svg>555 210 4471</li>
        <li><svg viewBox="0 0 12 12"><path d="M3.5 0h5a1 1 0 0 1 1 1v10a1 1 0 0 1-1 1h-5a1 1 0 0 1-1-1V1a1 1 0 0 1 1-1zm.5 1.5v8h4v-8z"/></svg>555 388 9025</li>
        <li><svg viewBox="0 0 12 12"><path d="M3 0h6v3H3zM1 4h10v5H9v3H3V9H1zm3 4v3h4V8z"/></svg>555 746 1302</li>
        <li><svg viewBox="0 0 12 12"><path d="M0 2h12v8H0zm1 1v.4L6 7l5-3.6V3z"/></svg>hello@tavu.com</li>
        <li><svg viewBox="0 0 12 12"><circle cx="6" cy="6" r="6"/></svg>www.tavu.com</li>
      </ul>
    </div>
    <div class="bottom-band"></div>
  </section>
</div>
</body>
</html>
```